Фирменный стиль для Trelk
Визитка, Поздравительная открытка, Футболка
Всем привет!)
Мы компания которая занимается практически всем что связано с виртуальной реальностью и игровыми технологиями, а именно:
- У нас свой VR-клуб
- Магазин по продаже игровых консолей и VR систем
- Сервисный центр по ремонту оборудования (VR и консоли)
Нужно создать фирменный стиль, взяв за основу наш логотип, в первую очередь нам нужны визитка, подарочный сертификат в конверте и листовка А5.
Задача осложняется тем что у нас разнообразные сферы деятельности и нужно сделать так чтобы промо материалы можно было легко переделывать под нужную сферу, например листовку, для рекламы клуба и для рекламы магазина или сделать 3 отдельных объединенных общим лого и цветовой гаммой, как будет лучше.?
Из пожеланий хотелось бы видеть легкость и минимализм. Удачный, на наш взгляд, пример:
https://www.folioplex.net/gallery/48213906/Norvo-Rebranding
Но необязательно опираться на него, нам хотелось бы увидеть ваш свежий взгляд.
Сам логотип можно слегка подправить, пропорции, расстояния между элементами, шрифт и т.д., но в целом нужно его сохранить, можно так же добавить разделение например ниже названия писать "сервисный центр" или "магазин" для смыслового разделения на бланках и визитках.
Если будут вопросы, смело задавайте, будем стараться отвечать максимально оперативно.
Всем успехов и заранее спасибо!)

```html
<!DOCTYPE html>
<html lang="ru">
<head>
<meta charset="UTF-8">
<title>Trelk — листовка A5</title>
<link href="https://fonts.googleapis.com/css2?family=Montserrat:wght@300;400;500;600;700&display=swap" rel="stylesheet">
<style>
  :root {
    --stage: #13232b;
    --flyer: #07080d;
    --white: #ffffff;
    --muted: #c9ccd6;
    --accent-blue: #2f8fe0;
    --neon-red: #e0263c;
    --neon-blue: #2a5bff;
    --violet: #3a1f5a;
  }
  * { box-sizing: border-box; margin: 0; padding: 0; }
  html, body {
    width: 1200px; height: 915px; overflow: hidden;
    background: var(--stage);
    font-family: "Montserrat", sans-serif;
    color: var(--white);
  }
  .flyer {
    position: absolute; left: 60px; top: 76px;
    width: 1080px; height: 764px;
    background: var(--flyer);
    overflow: hidden;
  }
  .flyer__visual {
    position: absolute; right: 0; top: 0;
    width: 68%; height: 100%;
    background:
      radial-gradient(ellipse 38% 34% at 62% 24%, rgba(224,38,60,0.75), transparent 70%),
      radial-gradient(ellipse 30% 30% at 84% 12%, rgba(42,91,255,0.55), transparent 70%),
      radial-gradient(ellipse 40% 30% at 70% 62%, rgba(224,38,60,0.45), transparent 70%),
      radial-gradient(ellipse 35% 40% at 40% 45%, rgba(58,31,90,0.8), transparent 70%),
      linear-gradient(90deg, var(--flyer) 0%, #0c0b18 35%, #150c1e 100%);
  }
  .brand {
    position: absolute; left: 64px; top: 62px;
    display: flex; align-items: center; gap: 16px;
  }
  .brand__mark { width: 40px; height: 40px; background: var(--accent-blue); }
  .brand__name { font-size: 50px; font-weight: 400; letter-spacing: 3px; color: var(--white); }
  .flyer__title {
    position: absolute; left: 64px; top: 172px;
    font-size: 36px; font-weight: 500; letter-spacing: 0.5px;
  }
  .flyer__lead {
    position: absolute; left: 64px; top: 236px; width: 640px;
    font-size: 15px; line-height: 1.6; color: var(--muted); font-weight: 400;
  }
  .flyer__tagline {
    position: absolute; left: 250px; top: 450px; width: 780px;
    text-align: center; text-transform: uppercase; white-space: nowrap;
    font-size: 28px; font-weight: 500; line-height: 1.25; letter-spacing: 0.3px;
  }
  .features {
    position: absolute; left: 280px; top: 570px; width: 720px;
    display: flex; justify-content: space-between; list-style: none;
  }
  .feature { width: 160px; display: flex; flex-direction: column; align-items: center; gap: 16px; }
  .feature svg { width: 68px; height: 56px; }
  .feature__label { font-size: 17px; font-weight: 600; text-align: center; line-height: 1.25; }
</style>
</head>
<body>
  <article class="flyer">
    <div class="flyer__visual" role="img" aria-label="Фото: человек в VR-шлеме среди неоновых красных и синих кубов"></div>

    <div class="brand">
      <span class="brand__mark"></span>
      <span class="brand__name">Trelk</span>
    </div>

    <h1 class="flyer__title">ВИРТУАЛЬНАЯ РЕАЛЬНОСТЬ</h1>
    <p class="flyer__lead">Наш клуб это место где Вы можете попробовать самые современные технологии в области виртуальной реальности. Мы создали уютное пространство для игр с друзьями, семьёй и коллегами. Каждая площадка оснащена новым оборудованием, а наши инструкторы помогут быстро освоиться. Приходите к нам и откройте для себя новые миры и яркие впечатления!</p>

    <h2 class="flyer__tagline">Всё для хорошего отдыха<br>у нас найдётся развлечение для каждого</h2>

    <ul class="features">
      <li class="feature">
        <svg viewBox="0 0 54 44" fill="none" stroke="#fff" stroke-width="2.5" stroke-linejoin="round">
          <rect x="6" y="12" width="42" height="22" rx="6"/>
          <path d="M6 22 H2 M48 22 H52"/>
          <path d="M22 34 Q27 28 32 34"/>
        </svg>
        <span class="feature__label">Шесть VR<br>площадок</span>
      </li>
      <li class="feature">
        <svg viewBox="0 0 54 44" fill="none" stroke="#fff" stroke-width="2.5" stroke-linejoin="round">
          <rect x="4" y="8" width="46" height="28" rx="4"/>
          <path d="M14 18 l6 6 M20 18 l-6 6 M34 18 l6 6 M40 18 l-6 6"/>
          <path d="M22 30 H32"/>
        </svg>
        <span class="feature__label">Более 50 игр</span>
      </li>
      <li class="feature">
        <svg viewBox="0 0 54 44" fill="none" stroke="#fff" stroke-width="2.5" stroke-linejoin="round">
          <rect x="20" y="4" width="14" height="11" rx="1"/>
          <rect x="5" y="29" width="14" height="11" rx="1"/>
          <rect x="35" y="29" width="14" height="11" rx="1"/>
          <path d="M27 15 V22 M12 29 V22 H42 V29"/>
        </svg>
        <span class="feature__label">Сетевые игры</span>
      </li>
      <li class="feature">
        <svg viewBox="0 0 54 44" fill="none" stroke="#fff" stroke-width="2.5" stroke-linejoin="round">
          <path d="M14 10 H40 Q50 10 51 24 Q52 38 44 36 L36 28 H18 L10 36 Q2 38 3 24 Q4 10 14 10 Z"/>
          <path d="M14 19 V25 M11 22 H17"/>
          <circle cx="37" cy="19" r="1.5"/>
          <circle cx="41" cy="23" r="1.5"/>
        </svg>
        <span class="feature__label">Приставки<br>Playtone</span>
      </li>
    </ul>
  </article>
</body>
</html>
```